Professional modern business card design

A business card for my nutrition business, wanting a professional look, with info clearly visible. Open to using logo colours too.

Would like key info on the front -
logo
my name and qualifications
email
phone number

and just an enlarged logo again / image on the back.

```html
<!DOCTYPE html>
<html lang="en">
<head>
<meta charset="utf-8">
<title>Fernway Nutrition – Business Card</title>
<link href="https://fonts.googleapis.com/css2?family=Montserrat:wght@400;500;600&display=swap" rel="stylesheet">
<style>
  :root {
    --navy: #03243f;
    --navy-light: #0d3452;
    --lime: #cddc00;
    --white: #ffffff;
    --paper: #f6f6f6;
    --ink: #2b2b2b;
    --backdrop: #3a3a3a;
  }
  * { box-sizing: border-box; margin: 0; padding: 0; }
  html, body {
    width: 1200px; height: 1200px; overflow: hidden;
    background: var(--backdrop);
  }
  .canvas { position: relative; width: 1200px; height: 1200px; }

  .card {
    position: absolute; left: 160px; width: 880px; height: 503px;
    border-radius: 34px; overflow: hidden;
  }

  /* ---------- Brand name ---------- */
  .brand-name {
    position: absolute; display: flex; align-items: center;
    font-family: "Montserrat", sans-serif; font-weight: 600;
    line-height: 1; white-space: nowrap;
  }
  .brand-name__square { flex: none; background: var(--lime); }

  /* ---------- Front ---------- */
  .card--front {
    top: 70px;
    background: linear-gradient(180deg, var(--white) 0%, var(--paper) 100%);
  }
  .card--front .brand-name {
    right: 70px; top: 190px; gap: 16px;
    color: var(--navy); font-size: 40px;
  }
  .card--front .brand-name__square { width: 26px; height: 26px; }

  .identity {
    position: absolute; left: 70px; top: 250px;
    padding-left: 18px; border-left: 7px solid var(--lime);
    font-family: "Montserrat", sans-serif;
  }
  .identity__name {
    color: var(--lime); font-size: 44px; font-weight: 400; line-height: 1;
    letter-spacing: 0.5px;
  }
  .identity__title {
    color: var(--ink); font-size: 18px; font-weight: 500; letter-spacing: 1px;
    margin-top: 4px;
  }

  .contacts {
    position: absolute; left: 100px; top: 360px; list-style: none;
    font-family: "Montserrat", sans-serif; font-size: 26px; color: var(--ink);
  }
  .contacts li { display: flex; align-items: center; gap: 16px; height: 40px; }
  .contacts svg { width: 28px; height: 28px; flex: none; }

  .band { position: absolute; bottom: 0; height: 22px; }
  .band--lime { left: 0; width: 62%; background: var(--lime); }
  .band--navy { left: 63%; right: 0; background: var(--navy); }

  /* ---------- Back ---------- */
  .card--back {
    top: 627px;
    background: linear-gradient(100deg, var(--navy) 0%, var(--navy) 40%, var(--navy-light) 55%, var(--navy) 75%);
  }
  .card--back .brand-name {
    left: 110px; right: 70px; top: 190px; gap: 24px; justify-content: center;
    color: var(--lime); font-size: 68px;
  }
  .card--back .brand-name__square { width: 44px; height: 44px; }
  .accent-bar {
    position: absolute; left: 45%; right: 9%; bottom: 58px; height: 30px;
    background: var(--lime);
  }
</style>
</head>
<body>
<main class="canvas">

  <section class="card card--front" aria-label="Card front">
    <div class="brand-name">
      <span class="brand-name__square" aria-hidden="true"></span>
      <span>Fernway Nutrition</span>
    </div>

    <div class="identity">
      <p class="identity__name">JOHN DOE</p>
      <p class="identity__title">NUTRITIONIST</p>
    </div>

    <ul class="contacts">
      <li>
        <svg viewBox="0 0 24 24" aria-hidden="true"><path fill="#cddc00" d="M6.6 10.8a15.1 15.1 0 0 0 6.6 6.6l2.2-2.2c.3-.3.7-.4 1-.2 1.1.4 2.3.6 3.6.6.6 0 1 .4 1 1V20c0 .6-.4 1-1 1A17 17 0 0 1 3 4c0-.6.4-1 1-1h3.5c.6 0 1 .4 1 1 0 1.3.2 2.5.6 3.6.1.3 0 .7-.2 1z"/></svg>
        <span>(000) 000 0000</span>
      </li>
      <li>
        <svg viewBox="0 0 24 24" aria-hidden="true"><rect x="2" y="5" width="20" height="14" fill="#cddc00"/><path d="M2 5l10 8 10-8M2 19l7.5-7M22 19l-7.5-7" fill="none" stroke="#ffffff" stroke-width="1.5"/></svg>
        <span>email@youremail.com</span>
      </li>
    </ul>

    <div class="band band--lime"></div>
    <div class="band band--navy"></div>
  </section>

  <section class="card card--back" aria-label="Card back">
    <div class="brand-name">
      <span class="brand-name__square" aria-hidden="true"></span>
      <span>Fernway Nutrition</span>
    </div>
    <div class="accent-bar"></div>
  </section>

</main>
</body>
</html>
```